Business Card Design

We are a business based in Sydney repairing and restoring timber windows. We mainly cater to residential home owners although sometimes work with larger building companies. We do a lot of work in heritage buildings though also cater to modern windows.
Our Logo is Black and Gold and were thinking of using a white card with only these two colours although we are open to any design suggestions. Check out our website for ideas.
Front of Card
Contact Information, Website & Business Name
Back of Card
Business Logo, website?
Target Market(s)
Home Owners
Industry/Entity Type
Residential
Contact Information for Business Card
Casement Craft Renewals
Owen Castell
0457 302 689
owen@casementcraftrenewals.com
www.casementcraftrenewals.com
Look and feel

```html
<!DOCTYPE html>
<html lang="en">
<head>
<meta charset="utf-8">
<title>Casement Craft Renewals – Business Card</title>
<link rel="stylesheet" href="https://fonts.googleapis.com/css2?family=Open+Sans:wght@400;600&display=swap">
<style>
  :root {
    --bg: #d9d9d7;
    --paper: #fbfbf9;
    --ink: #1b1b1b;
    --card-black: #151515;
    --gold: #c1912d;
    --white: #ffffff;
    --muted: #d6d6d6;
    --gloss: #3c3c3c;
  }
  * { margin: 0; padding: 0; box-sizing: border-box; }
  html, body { width: 1200px; height: 775px; overflow: hidden; }
  body {
    background: var(--bg);
    font-family: "Open Sans", Arial, sans-serif;
    position: relative;
  }
  .card {
    position: absolute;
    top: 245px;
    width: 500px;
    height: 286px;
    border-radius: 18px;
    overflow: hidden;
    box-shadow: 0 6px 18px rgba(0,0,0,.18);
  }
  .card--front { left: 70px; background: var(--paper); }
  .card--back { left: 630px; background: var(--card-black); }

  /* front */
  .front-brand {
    position: absolute; left: 34px; top: 34px;
    display: flex; align-items: center; gap: 12px;
    color: var(--ink); font-size: 26px; font-weight: 400; line-height: 1.1;
  }
  .brand-mark { width: 14px; height: 14px; background: var(--gold); flex: none; }
  .tagline-band {
    position: absolute; left: 0; right: 0; top: 158px; height: 22px;
    background: var(--gold); color: var(--white);
    font-size: 12.5px; line-height: 22px; padding-left: 22px; letter-spacing: .2px;
  }
  .contact-panel {
    position: absolute; left: 0; right: 0; top: 180px; bottom: 0;
    background: var(--card-black); color: var(--white);
  }
  .holder-name {
    position: absolute; left: 28px; top: 52px;
    font-size: 19px; font-weight: 400;
  }
  .divider {
    position: absolute; left: 205px; top: 16px; width: 1px; height: 72px;
    background: #555;
  }
  .contact-list { position: absolute; left: 222px; top: 18px; list-style: none; }
  .contact-list li {
    display: flex; align-items: center; gap: 7px;
    font-size: 11.5px; line-height: 22px; color: var(--muted);
  }
  .contact-list li.phone { color: var(--white); font-weight: 600; }
  .contact-icon { width: 13px; height: 13px; flex: none; }

  /* back */
  .back-brand {
    position: absolute; left: 0; right: 0; top: 62px;
    text-align: center; color: var(--gloss);
    font-size: 40px; font-weight: 400; line-height: 1.15;
  }
  .back-web {
    position: absolute; left: 0; right: 0; bottom: 40px;
    text-align: center; color: var(--white); font-size: 15px;
  }
</style>
</head>
<body>

<section class="card card--front" aria-label="Business card front">
  <div class="front-brand">
    <span class="brand-mark"></span>
    <span class="brand-name">Casement Craft<br>Renewals</span>
  </div>
  <div class="tagline-band">Sydney's Timber Windows Repair and Replacement Specialist</div>
  <div class="contact-panel">
    <p class="holder-name">Owen Castell</p>
    <span class="divider"></span>
    <ul class="contact-list">
      <li class="phone">
        <svg class="contact-icon" viewBox="0 0 13 13"><rect width="13" height="13" rx="2" fill="#c1912d"/><path d="M4 3.2l1.3 1.6-.7.9c.5 1 1.3 1.9 2.4 2.4l.9-.7 1.6 1.3-.8 1.1C6.3 9.6 3.4 6.7 3 4z" fill="#151515"/></svg>
        0457 302 689
      </li>
      <li>
        <svg class="contact-icon" viewBox="0 0 13 13"><rect width="13" height="13" rx="2" fill="#c1912d"/><rect x="3" y="4" width="7" height="5" fill="none" stroke="#151515" stroke-width="1"/><path d="M3 4l3.5 2.8L10 4" fill="none" stroke="#151515" stroke-width="1"/></svg>
        owen@casementcraftrenewals.com
      </li>
      <li>
        <svg class="contact-icon" viewBox="0 0 13 13"><rect width="13" height="13" rx="2" fill="#c1912d"/><circle cx="6.5" cy="6.5" r="3.5" fill="none" stroke="#151515" stroke-width="1"/><path d="M3 6.5h7M6.5 3c-1.6 2.2-1.6 4.8 0 7M6.5 3c1.6 2.2 1.6 4.8 0 7" fill="none" stroke="#151515" stroke-width=".8"/></svg>
        www.casementcraftrenewals.com
      </li>
    </ul>
  </div>
</section>

<section class="card card--back" aria-label="Business card back">
  <div class="back-brand">Casement<br>Craft Renewals</div>
  <p class="back-web">www.casementcraftrenewals.com</p>
</section>

</body>
</html>
```